Flyer-Design für Lumira Afghan Take Away
Zielgruppe
Gastrobetrieb mit Afghanischer Küche. Hauptangebot: Reisgerichte, Teigtaschen und Korma (Currygerichte). ZG: Studenten/Schüller, Ladenbesitzer und Passanten, da es sehr Zentral liegt
Aufgabenstellung
Öffnungszeiten:
MO: 11:30-14h
DI&MI: 11:30-14h/18h-20h
DO&FR: 11:30-14h/18h-21h
SA: 11:30-15h
SO: Geschlossen
INFO: www.lumira-imbiss.ch

```html
<!DOCTYPE html>
<html lang="de">
<head>
<meta charset="utf-8">
<title>Lumira Afghan Take Away – Flyer</title>
<link rel="stylesheet" href="https://fonts.googleapis.com/css2?family=Ubuntu:wght@400;500;700&family=Roboto+Condensed:wght@400;700&display=swap">
<style>
:root{
  --bg:#ececec;
  --maroon:#8e2b2b;
  --red:#c8102e;
  --ink:#222;
  --muted:#555;
  --paper:#e9e8e6;
  --card-top:#f1e6da;
  --card-bottom:#d9b48a;
  --green:#2f6b2f;
  --white:#fff;
}
*{box-sizing:border-box;margin:0;padding:0}
html,body{width:1200px;height:1200px;overflow:hidden;background:var(--bg);font-family:"Ubuntu",sans-serif;color:var(--ink)}
.canvas{position:relative;width:1200px;height:1200px}

/* front side */
.front{position:absolute;left:150px;top:120px;width:420px;height:960px;background:var(--white);box-shadow:0 6px 18px rgba(0,0,0,.18)}
.dish-list{position:absolute;left:18px;top:18px;width:250px}
.dish-card{position:relative;height:184px;margin-bottom:16px;border-radius:6px;overflow:hidden;background:linear-gradient(#fbf7f2,#f3ede6)}
.dish-card h3{font-family:"Roboto Condensed",sans-serif;font-weight:700;color:var(--red);font-size:15px;padding:10px 10px 2px}
.dish-card p{font-family:"Roboto Condensed",sans-serif;color:var(--red);font-size:9.5px;line-height:1.25;padding:0 10px}
.dish-photo{position:absolute;left:0;right:0;bottom:0;height:118px;background:radial-gradient(ellipse 42% 38% at 48% 55%,#fafafa 0 60%,#e8d6c0 62%,transparent 70%),linear-gradient(var(--card-top),var(--card-bottom))}
.price{position:absolute;right:12px;bottom:10px;width:52px;height:52px;border-radius:50%;background:var(--red);color:var(--white);font-family:"Roboto Condensed",sans-serif;font-size:21px;display:flex;align-items:center;justify-content:center}
.brand-side{position:absolute;left:282px;top:40px;width:126px;text-align:center}
.brand-name{font-family:"Ubuntu",sans-serif;font-weight:700;font-size:20px;color:var(--maroon);line-height:1.1}
.brand-mark{width:14px;height:14px;border-radius:50%;background:var(--maroon);margin:0 auto 8px}
.hours{position:absolute;left:290px;top:730px;width:420px;transform:rotate(-90deg);transform-origin:0 0;font-family:"Roboto Condensed",sans-serif;font-weight:700;font-size:14.5px;line-height:1.35;color:var(--ink)}
.hours .lbl{color:var(--red);text-decoration:underline}
.hours b{color:var(--red)}
.hours .web{color:var(--green)}
.front-foot{position:absolute;left:0;right:0;bottom:0;height:152px;background:var(--maroon);display:flex;align-items:center}
.foot-brand{width:130px;text-align:center;color:var(--white);font-weight:700;font-size:19px;line-height:1.15}
.foot-brand .brand-mark{background:var(--white)}
.divider{width:0;height:92px;border-left:3px dotted var(--white);margin:0 18px}
.address{display:flex;align-items:flex-start;gap:8px;color:var(--white);font-weight:700;font-size:19px;line-height:1.2}
.address svg{flex:none;margin-top:2px}

/* back side */
.back{position:absolute;left:630px;top:120px;width:420px;height:960px;background:linear-gradient(160deg,#f2f1ef,var(--paper) 55%,#dedcd9);box-shadow:0 6px 18px rgba(0,0,0,.18);overflow:hidden}
.back-top{position:absolute;left:0;top:0;width:420px;height:140px}
.menu{position:absolute;left:22px;right:20px;top:120px}
.menu h2{color:var(--red);font-size:14px;font-weight:700;margin:4px 0 4px 26px}
.row{position:relative;display:grid;grid-template-columns:42px 1fr 58px;border-bottom:1px solid var(--red);padding:3px 0 4px}
.day{color:var(--red);font-weight:700;font-size:14px}
.dish{font-weight:700;font-size:15px;line-height:1.1}
.desc{font-size:7.5px;color:var(--muted);line-height:1.25;margin-top:1px}
.amt{align-self:end;text-align:right;font-weight:700;font-size:14px}
.chf{position:absolute;right:0;top:2px;font-size:7px;color:var(--muted)}
.note{position:absolute;right:22px;top:826px;font-size:7.5px;color:var(--red)}
.back-foot{position:absolute;left:0;right:0;bottom:0;height:110px;background:var(--maroon);display:flex;align-items:center;padding-left:18px}
</style>
</head>
<body>
<div class="canvas">

  <section class="front" aria-label="Vorderseite">
    <div class="dish-list">
      <article class="dish-card">
        <h3>Mantu</h3>
        <p>Gedämpfte Rindhackfleischtaschen aus frischem Teig, dazu Tomatensauce mit gelben Erbsen und Joghurt-Minze-Sauce</p>
        <div class="dish-photo" role="img" aria-label="Foto: Mantu-Teigtaschen mit Tomatensauce in weisser Schale"></div>
        <span class="price">14.-</span>
      </article>
      <article class="dish-card">
        <h3>Ashak</h3>
        <p>Gedämpfte Lauchtaschen aus frischem Teig, dazu Tomatensauce mit gelben Erbsen und Joghurt-Minze-Sauce</p>
        <div class="dish-photo" role="img" aria-label="Foto: Ashak-Lauchtaschen in weisser Schale"></div>
        <span class="price">14.-</span>
      </article>
      <article class="dish-card">
        <h3>Chapli-Kabob im Taschenbrot</h3>
        <p>Gebratene Rindshacksteaks mit Gemüse, Salat, Chili-Koriander und Joghurt-Minze-Sauce</p>
        <div class="dish-photo" role="img" aria-label="Foto: Chapli-Kabob im gefüllten Taschenbrot"></div>
        <span class="price">9.-</span>
      </article>
      <article class="dish-card">
        <h3>Sambosa 2 Stk.</h3>
        <p>Frittierte Kartoffel oder Gemüsetaschen, dazu Chili-Koriandersauce und Joghurt-Minze-Sauce</p>
        <div class="dish-photo" role="img" aria-label="Foto: zwei Sambosa mit Saucen in weisser Schale"></div>
        <span class="price">6.-</span>
      </article>
    </div>

    <div class="brand-side">
      <div class="brand-mark"></div>
      <div class="brand-name">Lumira<br>Afghan<br>Take Away</div>
    </div>

    <div class="hours">
      <div class="lbl">Öffnungszeiten:</div>
      <div><b>MO:</b> 11:30-14h &nbsp;-&nbsp; <b>DI&amp;MI:</b> 11:30-14h/18h-20h</div>
      <div><b>DO&amp;FR:</b> 11:30-14h/18h-21h</div>
      <div><b>SA:</b> 11:30-15h &nbsp;-&nbsp; <b>SO:</b> Geschlossen</div>
      <div class="web">www.lumira-imbiss.ch</div>
    </div>

    <footer class="front-foot">
      <div class="foot-brand"><div class="brand-mark"></div>Lumira<br>Take Away</div>
      <div class="divider"></div>
      <div class="address">
        <svg width="16" height="22" viewBox="0 0 16 22"><path d="M8 1a7 7 0 0 0-7 7c0 5 7 13 7 13s7-8 7-13a7 7 0 0 0-7-7z" fill="none" stroke="#fff" stroke-width="2"/><circle cx="8" cy="8" r="2.5" fill="#fff"/></svg>
        <div>Lindenweg 21<br>8004 Zürich</div>
      </div>
    </footer>
  </section>

  <section class="back" aria-label="Rückseite">
    <svg class="back-top" viewBox="0 0 420 140" preserveAspectRatio="none"><path d="M0 0H420V34C300 80 160 120 0 112Z" fill="#8e2b2b"/></svg>
    <div class="menu">
      <h2>HAUSGEMACHTE MITTAGSMENÜ:</h2>
      <div class="row"><span class="day">MO:</span><div><div class="dish">Lawang</div><div class="desc">Pouletbrustgeschn. in Kurkuma-Joghurt-Sauce und frischen Kräuter, dazu Brechbohnen Qorma und Basmatireis</div></div><span class="amt">14.50</span><span class="chf">CHF</span></div>
      <div class="row"><span class="day">DI:</span><div><div class="dish">Qorma Tschalau</div><div class="desc">Basmatireis mit würzigem Rindfleisch, dazu Sabzi (gebratener Spinat)</div></div><span class="amt">14.50</span></div>
      <div class="row"><span class="day">MI:</span><div><div class="dish">Kofta Tschalau</div><div class="desc">Basmatireis mit Kofta (Afgh. Meatballs), Dal (Linsen)</div></div><span class="amt">14.50</span></div>
      <div class="row"><span class="day">DO:</span><div><div class="dish">Kabuli-Palau mit Pouletfleisch</div><div class="desc">Brauner Basmatireis mit Karottenstreifen, Rosinen, gekochtem Pouletfleisch und Qorme-e Gulpi</div></div><span class="amt">14.50</span></div>
      <div class="row"><span class="day"></span><div><div class="dish">Kabuli-Palau mit Lamm-Qorma</div><div class="desc">Brauner Basmati-Reis mit Karottenstr., Rosinen, Lamm-Qorma und Qorme-e Gulpi</div></div><span class="amt">16.50</span></div>
      <div class="row"><span class="day">FR:</span><div><div class="dish">Mahi Tschalau</div><div class="desc">Basmatireis mit Fisch-Qorma und Qorm-e Sabzi (gebratener Spinat mit Bohnen)</div></div><span class="amt">14.50</span></div>
      <div class="row"><span class="day"></span><div><div class="dish">Lawang</div><div class="desc">Pouletgeschn. in Kurkuma-Joghurt-Sauce und fr. Kräuter, Qorm-e Sabzi, Basmatireis</div></div><span class="amt">14.50</span></div>
      <div class="row"><span class="day">SA:</span><div><div class="dish">Kabuli-Palau mit Pouletfleisch</div><div class="desc">Brauner Basmatireis mit Karottenstreifen, Rosinen, gekochtem Pouletfleisch und Qorme-e Gulpi</div></div><span class="amt">14.50</span></div>
      <div class="row"><span class="day"></span><div><div class="dish">Kabuli-Palau mit Lamm-Qorma</div><div class="desc">Brauner Basmati-Reis mit Karottenstreifen, Rosinen, Lamm-Qorma und Qorme-e Gulpi</div></div><span class="amt">16.50</span></div>
      <h2>TÄGLICHES ANGEBOT:</h2>
      <div class="row"><span class="day"></span><div><div class="dish">Mantu</div><div class="desc">Gedämpfte Rindhackfleischtaschen aus frischem Teig, dazu Tomatensauce mit gelben Erbsen und Joghurt-Minze-Sauce</div></div><span class="amt">14.00</span></div>
      <div class="row"><span class="day"></span><div><div class="dish">Ashak</div><div class="desc">Gedämpfte Lauchtaschen aus frischem Teig, dazu Tomatensauce mit gelben Erbsen und Joghurt-Minze-Sauce</div></div><span class="amt">14.00</span></div>
      <div class="row"><span class="day"></span><div><div class="dish">Chapli-Kabob im Taschenbrot</div><div class="desc">Gebratene Rindshacksteaks mit Gemüse, Salat, Chili-Koriander und Joghurt-Minze-Sauce</div></div><span class="amt">9.00</span></div>
      <div class="row"><span class="day"></span><div><div class="dish">2 Stk. Sambosa</div><div class="desc">Frittierte Kartoffel oder Gemüsetaschen, dazu Chili-Koriandersauce und Joghurt-Minze-Sauce</div></div><span class="amt">6.00</span></div>
      <div class="row"><span class="day"></span><div><div class="dish">Unsere Empfehlung: Lumira-Teller</div><div class="desc">Tages-Menü und Teigtaschen</div></div><span class="amt">19.50</span></div>
    </div>
    <p class="note">Wir haben auch Studenten-Rabatt!</p>
    <footer class="back-foot">
      <div class="foot-brand"><div class="brand-mark"></div>Lumira<br>Take Away</div>
      <div class="divider"></div>
      <div class="address">
        <svg width="16" height="22" viewBox="0 0 16 22"><path d="M8 1a7 7 0 0 0-7 7c0 5 7 13 7 13s7-8 7-13a7 7 0 0 0-7-7z" fill="none" stroke="#fff" stroke-width="2"/><circle cx="8" cy="8" r="2.5" fill="#fff"/></svg>
        <div>Lindenweg 21<br>8004 Zürich</div>
      </div>
    </footer>
  </section>

</div>
</body>
</html>
```